Design a book cover for "The Harvester's Ledger"

We need a book cover for a book titled "The Harvester's Ledger" The subtitle is "Why Machines Deliver a Shared Dividend, the Close of Levy Systems, and a Steady Treasury"
You can use one of the attached files of cover art, or come up with your own art - designer's choice!
Author's Name is Brent Hallow
We'd like the copy in the attached file "Back Cover" on the back cover, along with the copy in "About the Author" and the author's photo on the back cover.
Updates

Project Deadline Extended Reason: The deadline has been extended to give time for designers to respond to comments. Feel free to submit designs that do not use the cover art graphics attached to the brief - that art was meant as a suggestion. Added Sunday, January 15, 2017

Target Market(s)

Layperson

Font styles to use
Sans Serif

Colors
0456a4
3176b5
85abd2
0293ce
33a6d7
85cae6
1b1b1b
474747
919191

Requirements
Nice to have
• We'd like to see how the horse and rider would look on the front cover. The attached file, "Pendlewick Option", is a rough sketch. The artist is refining it, adding color, and will have the rider carrying modern technology instead of scrolls.
• We are open to all colors, but have indicated some colors we like.

```html
<!DOCTYPE html>
<html lang="en">
<head>
<meta charset="UTF-8">
<title>The Harvester's Ledger — Book Cover</title>
<link href="https://fonts.googleapis.com/css2?family=Oswald:wght@400;500;600&display=swap" rel="stylesheet">
<style>
  :root {
    --stage: #e9e9e9;
    --paper: #ffffff;
    --title-blue: #1f5a9c;
    --subtitle-grey: #6a6a6a;
    --art-grey: #c6c6c6;
  }
  html, body {
    margin: 0;
    padding: 0;
    width: 1200px;
    height: 1200px;
    overflow: hidden;
    background: var(--stage);
  }
  .canvas {
    position: relative;
    width: 1200px;
    height: 1200px;
  }
  .cover {
    position: absolute;
    left: 220px;
    top: 30px;
    width: 760px;
    height: 1140px;
    background: var(--paper);
    box-shadow: 0 4px 18px rgba(0,0,0,0.12);
    overflow: hidden;
    font-family: 'Oswald', sans-serif;
  }
  .cover-art {
    position: absolute;
    left: 120px;
    top: 470px;
    width: 520px;
    height: 540px;
    border-radius: 50%;
    background: var(--art-grey);
  }
  .subtitle {
    position: absolute;
    top: 88px;
    left: 70px;
    right: 70px;
    margin: 0;
    text-align: center;
    font-weight: 500;
    font-size: 25px;
    line-height: 1.35;
    letter-spacing: 1.5px;
    text-transform: uppercase;
    color: var(--subtitle-grey);
  }
  .title {
    position: absolute;
    top: 185px;
    left: 0;
    right: 0;
    margin: 0;
    text-align: center;
    font-weight: 600;
    text-transform: uppercase;
    color: var(--title-blue);
    white-space: nowrap;
  }
  .title-article {
    display: block;
    font-size: 80px;
    line-height: 1.05;
    letter-spacing: 2px;
  }
  .title-line {
    display: block;
    font-size: 116px;
    line-height: 1.02;
    letter-spacing: 1px;
  }
  .author {
    position: absolute;
    left: 0;
    right: 0;
    top: 930px;
    margin: 0;
    text-align: center;
    font-weight: 500;
    font-size: 62px;
    line-height: 1;
    letter-spacing: 22px;
    text-indent: 22px;
    text-transform: uppercase;
    white-space: nowrap;
    color: var(--title-blue);
  }
</style>
</head>
<body>
<div class="canvas">
  <section class="cover">
    <div class="cover-art" role="img" aria-label="Grey circle with line art of a cloud linked by circuit lines to dollar-sign tags"></div>
    <p class="subtitle">Why Machines Deliver a Shared Dividend, the Close of Levy Systems, and a Steady Treasury</p>
    <h1 class="title">
      <span class="title-article">The</span>
      <span class="title-line">Harvester's</span>
      <span class="title-line">Ledger</span>
    </h1>
    <p class="author">Brent Hallow</p>
  </section>
</div>
</body>
</html>
```